Wendale Ridge Concrete Pumping needs a logo design and is in the concrete industry

A creative design for this Wendale Ridge Concrete Pumping business. Using a trailer mounted line pump, not a boom pump.
Colour to be used is orange and a mix of white or black writing.
Target Market(s)
General Public, anyone
Industry/Entity Type
Concrete
Contact Information for Business Card
Wendale Ridge Concrete Pumping
Callum Hesketh
PO BOX 47
Birchmoor VIC 3264
Phone: 0417952803
Email: Hesketh@bluewrenmail.com.au
Colors
f37122
000000
ffffff
Requirements
Must have
- Details listed
Nice to have
- A great logo
Should not have
- anything silly

```html
<!DOCTYPE html>
<html lang="en">
<head>
<meta charset="utf-8">
<title>Wendale Ridge Concrete Pumping – Business Card</title>
<link rel="stylesheet" href="https://fonts.googleapis.com/css2?family=Arimo:wght@400;700&display=swap">
<style>
  :root {
    --orange: #f37122;
    --black: #0d0d0d;
    --card: #141414;
    --white: #ffffff;
    --grey: #6e6e6e;
    --emboss: #2a2a2a;
    --backdrop: #e6e3e0;
  }
  * { margin: 0; padding: 0; box-sizing: border-box; }
  html, body { width: 1200px; height: 716px; overflow: hidden; }
  body {
    background: var(--backdrop);
    font-family: "Arimo", Arial, sans-serif;
    position: relative;
  }
  .card {
    position: absolute;
    top: 193px;
    width: 540px;
    height: 330px;
    background: var(--card);
    overflow: hidden;
  }
  .card--front { left: 40px; }
  .card--back { left: 620px; }

  .brand {
    display: flex;
    align-items: center;
    gap: 12px;
  }
  .brand__mark {
    width: 22px; height: 22px;
    border-radius: 50%;
    flex: none;
  }
  .brand__name {
    font-weight: 700;
    line-height: 1.15;
    letter-spacing: 0.02em;
    white-space: nowrap;
  }

  .card--front .brand {
    position: absolute;
    left: 0; right: 0; top: 118px;
    justify-content: center;
  }
  .card--front .brand__mark { background: var(--emboss); width: 30px; height: 30px; }
  .card--front .brand__name { color: var(--emboss); font-size: 30px; }

  .card--back .brand {
    position: absolute;
    right: 40px; top: 58px;
  }
  .card--back .brand__mark { background: var(--orange); }
  .card--back .brand__name { color: var(--grey); font-size: 20px; }

  .holder {
    position: absolute;
    left: 30px; top: 128px;
    color: var(--orange);
    font-size: 15px;
    text-transform: uppercase;
    letter-spacing: 0.01em;
  }
  .rule {
    position: absolute;
    left: 30px; top: 152px;
    width: 450px; height: 2px;
    background: var(--orange);
  }
  .contact {
    position: absolute;
    left: 30px; top: 168px;
    list-style: none;
    color: var(--white);
    font-size: 15px;
  }
  .contact li {
    display: flex;
    align-items: center;
    gap: 8px;
    height: 23px;
  }
  .contact svg { width: 13px; height: 13px; flex: none; }

  .address {
    position: absolute;
    right: 30px; top: 262px;
    color: var(--white);
    font-size: 15px;
  }
  .footer-band {
    position: absolute;
    left: 0; bottom: 0;
    width: 540px; height: 50px;
  }
</style>
</head>
<body>

  <section class="card card--front" aria-label="Card front">
    <div class="brand">
      <span class="brand__mark"></span>
      <span class="brand__name">Wendale Ridge<br>Concrete Pumping</span>
    </div>
  </section>

  <section class="card card--back" aria-label="Card back">
    <div class="brand">
      <span class="brand__mark"></span>
      <span class="brand__name">Wendale Ridge<br>Concrete Pumping</span>
    </div>

    <p class="holder">Callum Hesketh</p>
    <div class="rule"></div>

    <ul class="contact">
      <li>
        <svg viewBox="0 0 13 13" aria-hidden="true">
          <rect width="13" height="13" rx="2" fill="#f37122"/>
          <path d="M4 3 L5.5 3 L6 5 L5 5.8 C5.6 7 6.2 7.6 7.2 8 L8 7 L10 7.5 L10 9 C7 9.5 3.5 6 4 3 Z" fill="#141414"/>
        </svg>
        0417952803
      </li>
      <li>
        <svg viewBox="0 0 13 13" aria-hidden="true">
          <rect y="2" width="13" height="9" fill="#f37122"/>
          <path d="M0.5 2.5 L6.5 7 L12.5 2.5" fill="none" stroke="#141414" stroke-width="1.2"/>
        </svg>
        Hesketh@bluewrenmail.com.au
      </li>
    </ul>

    <p class="address">PO BOX 47 Birchmoor VIC 3264</p>

    <svg class="footer-band" viewBox="0 0 540 50" aria-hidden="true">
      <path d="M0 10 L270 10 C292 10 300 22 312 30 L0 30 Z" fill="#5a5a5a"/>
      <path d="M0 30 L300 30 C318 30 322 12 345 12 L540 12 L540 50 L0 50 Z" fill="#f37122"/>
    </svg>
  </section>

</body>
</html>
```